Business cards and logo for a international shipping company called Harborline Freight LLC. We would like to incorporate the colors red and blue. We would like the theme to be nautical.

Industry/Entity Type

Business

```html
<!DOCTYPE html>
<html lang="en">
<head>
<meta charset="utf-8">
<title>Harborline Freight LLC – Business Cards</title>
<link rel="stylesheet" href="https://fonts.googleapis.com/css2?family=Open+Sans:wght@400;600;700;800&display=swap">
<style>
  :root {
    --navy: #0f3a8c;
    --red: #b80000;
    --pink: #f3c9c9;
    --white: #ffffff;
    --wave-white: #e9eef7;
    --card-black: #1e1e1f;
    --logo-red: #c8141e;
    --backdrop: #ece8e4;
  }
  * { margin: 0; padding: 0; box-sizing: border-box; }
  html, body { width: 1200px; height: 900px; overflow: hidden; }
  body {
    background: var(--backdrop);
    font-family: "Open Sans", Arial, sans-serif;
    position: relative;
  }
  .card {
    position: absolute;
    overflow: hidden;
    box-shadow: 0 6px 18px rgba(0,0,0,0.18);
  }
  .card-front { left: 78px; top: 35px; width: 587px; height: 362px; }
  .card-back {
    left: 388px; top: 505px; width: 566px; height: 351px;
    background: var(--card-black);
    display: flex; align-items: center; justify-content: center;
  }
  .card-art { position: absolute; inset: 0; width: 100%; height: 100%; }
  .brand-name {
    position: absolute;
    font-weight: 800;
    line-height: 0.98;
    text-transform: uppercase;
    letter-spacing: 0.5px;
  }
  .card-front .brand-name {
    left: 118px; top: 66px;
    font-size: 36px;
    color: var(--white);
  }
  .card-back .brand-name {
    position: static;
    font-size: 38px;
    color: var(--logo-red);
    transform: translate(26px, 16px);
  }
  .holder {
    position: absolute; left: 38px; top: 250px;
    color: var(--white);
  }
  .holder-name { font-size: 19px; font-weight: 700; letter-spacing: 0.3px; }
  .holder-title { font-size: 15px; font-weight: 400; margin-top: 1px; }
  .contact-list {
    position: absolute; left: 197px; top: 243px;
    list-style: none;
    color: var(--white);
    font-size: 15.5px;
    line-height: 22px;
  }
  .contact-list li { display: flex; align-items: center; gap: 7px; }
  .contact-list svg { width: 11px; height: 11px; fill: var(--white); flex: none; }
  .address {
    position: absolute; left: 39px; top: 318px;
    color: var(--white);
    font-size: 15px;
  }
</style>
</head>
<body>

  <section class="card card-front" aria-label="Business card front">
    <svg class="card-art" viewBox="0 0 587 362" preserveAspectRatio="none" aria-hidden="true">
      <rect width="587" height="362" fill="var(--navy)"/>
      <path d="M0,238 C170,190 400,155 587,136 L587,168 C400,182 180,208 0,252 Z" fill="var(--wave-white)"/>
      <path d="M0,250 C180,206 400,180 587,162 L587,362 L0,362 Z" fill="var(--red)"/>
      <path d="M110,236 C290,204 450,190 587,178 L587,188 C450,200 300,214 110,238 Z" fill="var(--pink)"/>
      <path d="M200,228 C340,212 470,203 587,196 L587,202 C470,209 340,218 200,230 Z" fill="var(--pink)" opacity="0.6"/>
    </svg>

    <div class="brand-name">Harborline<br>Freight</div>

    <div class="holder">
      <p class="holder-name">DANIEL REYES</p>
      <p class="holder-title">Managing Director</p>
    </div>

    <ul class="contact-list">
      <li>
        <svg viewBox="0 0 24 24"><path d="M6.6 10.8a15.1 15.1 0 0 0 6.6 6.6l2.2-2.2a1 1 0 0 1 1-.25 11.4 11.4 0 0 0 3.6.57 1 1 0 0 1 1 1V20a1 1 0 0 1-1 1A17 17 0 0 1 3 4a1 1 0 0 1 1-1h3.5a1 1 0 0 1 1 1c0 1.25.2 2.45.57 3.57a1 1 0 0 1-.25 1z"/></svg>
        044-555 018 273
      </li>
      <li>
        <svg viewBox="0 0 24 24"><path d="M2 5h20v14H2z M2 5l10 8 10-8" fill="var(--white)"/><path d="M3 6l9 7 9-7" fill="none" stroke="var(--red)" stroke-width="2"/></svg>
        info@harborlinefreight.com
      </li>
      <li>
        <svg viewBox="0 0 24 24"><circle cx="12" cy="12" r="10"/><path d="M2 12h20M12 2c3 3 3 17 0 20M12 2c-3 3-3 17 0 20M4 7h16M4 17h16" fill="none" stroke="var(--red)" stroke-width="1.5"/></svg>
        www.harborlinefreight.com
      </li>
    </ul>

    <p class="address">48 Quayside Road, Port District, Marlow Bay, 204117.</p>
  </section>

  <section class="card card-back" aria-label="Business card back">
    <div class="brand-name">Harborline<br>Freight</div>
  </section>

</body>
</html>
```